Web design for a Senior Home Care company

I want a web design for a home care company called Larkmoor Home Care. What LHC does is send caregivers into people's homes to assist with daily living needs such as companionship, food preparation, cleaning, bathing, using the bathroom, etc. Most of the clients are seniors. The people deciding to use LHC are usually the 50 year old children of these senior citizens. Most visitors to the site will be women searching for this service for their parents.

The call to action is to inspire the website visitors to call us to set up an appointment to meet them in their home. The site design should inspire confidence in Larkmoor Home Care to care for people's needs. We want to show the same attributes that a parent should have. Safety, Security and Loving Care.

Again, the goal of the site is to inspire and make it EASY for visitors to contact us either by phone call or through the website. The first choice is that they call us.

To help you with your ideas, In the attachments I've included different versions of our logo, a site map, examples of photos we might use and very rough draft of the website copy.

Target Market(s)

The customers will mostly be seniors. But, the people who will decide to use the company will the the 50 year old children of those seniors. Also, it is mostly women who are looking for help for their parents.

Industry/Entity Type

It Company

Number of Pages Required

5+ page

Requirements
Nice to have
• I want site visitors to easily be able to contact us with a phone call or through the website. The home page should inspire people to call us.

```html
<!DOCTYPE html>
<html lang="en">
<head>
<meta charset="utf-8">
<title>Larkmoor Home Care</title>
<link href="https://fonts.googleapis.com/css2?family=Oswald:wght@400;500;600&family=Open+Sans:wght@400;600&family=Roboto+Condensed:ital,wght@1,400;1,700&display=swap" rel="stylesheet">
<style>
:root{
  --brand:#1f7fc4;
  --nav:#1b74bd;
  --nav-active:#31a6e0;
  --accent:#2ca6df;
  --ink:#222;
  --body:#333;
  --tint:#e8f1f4;
  --line:#3b5a86;
  --footer:#2b2b2b;
  --white:#fff;
}
*{margin:0;padding:0;box-sizing:border-box}
html,body{width:1200px;height:2821px;overflow:hidden;background:var(--white)}
body{position:relative;font-family:"Open Sans",Arial,sans-serif;color:var(--body)}
.abs{position:absolute}
.heading{font-family:"Oswald",Arial,sans-serif;font-weight:500;color:var(--ink);text-transform:uppercase;letter-spacing:.3px}

/* header */
.site-header{left:0;top:0;width:1200px;height:98px;background:var(--white)}
.brand{left:71px;top:18px;display:flex;align-items:center;gap:10px}
.brand-mark{width:40px;height:40px;background:var(--brand)}
.brand-name{font-family:"Oswald",Arial,sans-serif;font-weight:500;font-size:26px;color:var(--brand);line-height:1}
.header-call{left:505px;top:30px;display:flex;align-items:center;gap:14px}
.header-call span{font-size:23px;color:#333}
.header-phone{left:900px;top:26px;font-family:"Oswald",Arial,sans-serif;font-weight:600;font-size:33px;color:#222}

/* nav */
.main-nav{left:0;top:98px;width:1200px;height:56px;background:var(--nav)}
.main-nav a{position:absolute;top:0;height:56px;line-height:56px;color:var(--white);text-decoration:none;font-weight:600;font-size:18px}
.main-nav a.active{background:var(--nav-active);padding:0 23px}

/* hero */
.hero{left:0;top:154px;width:1200px;height:501px;background:linear-gradient(100deg,#3f5a24 0%,#c9a44a 25%,#6e8a3a 45%,#d9c2a4 65%,#4f6a2c 85%,#3a4f22 100%)}

/* consultation */
.consult-title{left:56px;top:705px;font-size:37px;line-height:43px}
.consult-lede{left:56px;top:850px;width:440px;font-family:"Roboto Condensed",Arial,sans-serif;font-style:italic;font-size:20px;line-height:25px;color:#222}
.call-button{left:55px;top:955px;width:302px;height:49px;background:var(--accent);color:var(--white);font-family:"Oswald",Arial,sans-serif;font-weight:500;font-size:29px;line-height:49px;padding-left:18px}
.photo-frame{border:2px solid #dfe3e6}
.consult-photo{left:557px;top:715px;width:587px;height:395px;background:linear-gradient(120deg,#9fb4c6,#d8c8bb 55%,#7b8a96)}

/* services */
.services{left:0;top:1170px;width:1200px;height:704px;background:var(--tint)}
.services-photo{left:60px;top:1223px;width:403px;height:602px;border:3px solid var(--white);background:linear-gradient(160deg,#f3efe8,#4aa0c8 55%,#2b8ab8)}
.services-title{left:532px;top:1210px;font-size:37px}
.services-intro{left:532px;top:1273px;width:610px;font-family:"Roboto Condensed",Arial,sans-serif;font-style:italic;font-weight:700;font-size:17.5px;line-height:29px;color:#222}
.services-body{left:532px;top:1392px;width:620px;font-size:17px;line-height:29px;color:#222}
.service-list{left:537px;top:1510px;list-style:none}
.service-list li{display:flex;align-items:center;gap:12px;height:45px;font-weight:600;font-size:20px;color:#222}
.services-close{left:530px;top:1745px;width:560px;font-family:"Roboto Condensed",Arial,sans-serif;font-style:italic;font-weight:700;font-size:17.5px;line-height:29px;color:#222}

/* welcome */
.welcome-title{left:0;top:1932px;width:1200px;text-align:center;font-size:37px}
.welcome-copy{left:100px;top:1998px;width:1000px;text-align:center;font-size:17.5px;line-height:29px;color:#333}
.welcome-copy p+p{margin-top:29px}

/* contact */
.contact{left:0;top:2276px;width:1200px;height:485px;background:var(--tint)}
.contact-title{left:0;top:2306px;width:1200px;text-align:center;font-size:37px}
.contact-sub{left:0;top:2370px;width:1200px;text-align:center;font-size:24px;color:#222}
.field{background:var(--white);border:2px solid var(--line);font-size:14px;color:#444;padding:10px 12px}
.field svg{position:absolute;right:12px;top:12px}
.submit{left:515px;top:2675px;width:168px;height:49px;border-radius:25px;background:var(--accent);color:var(--white);text-align:center;line-height:49px;font-size:23px}

/* footer */
.site-footer{left:0;top:2761px;width:1200px;height:60px;background:var(--footer)}
.copyright{left:62px;top:20px;font-size:14.5px;color:#ddd}
.social{top:16px;width:28px;height:28px;border-radius:50%}
</style>
</head>
<body>

<header class="site-header abs">
  <div class="brand abs"><span class="brand-mark"></span><span class="brand-name">Larkmoor Home Care</span></div>
  <div class="header-call abs">
    <svg width="24" height="24" viewBox="0 0 24 24" aria-hidden="true"><path d="M6.6 10.8c1.4 2.8 3.8 5.1 6.6 6.6l2.2-2.2c.3-.3.7-.4 1-.2 1.1.4 2.3.6 3.6.6.6 0 1 .4 1 1V20c0 .6-.4 1-1 1C10.6 21 3 13.4 3 4c0-.6.4-1 1-1h3.5c.6 0 1 .4 1 1 0 1.3.2 2.5.6 3.6.1.3 0 .7-.2 1z" fill="#222"/></svg>
    <span>Call us to set up an appointment</span>
  </div>
  <div class="header-phone abs">555 - 210 - 318</div>
</header>

<nav class="main-nav abs">
  <a class="active" style="left:56px">Home</a>
  <a style="left:179px">About Us</a>
  <a style="left:301px">Services</a>
  <a style="left:416px">Free In-Home Consultation</a>
  <a style="left:692px">News</a>
  <a style="left:784px">FAQ</a>
  <a style="left:865px">Client Portal</a>
  <a style="left:1016px">Contact Us</a>
</nav>

<div class="hero abs" role="img" aria-label="Smiling caregiver with her hand on a senior woman's shoulder in a garden of yellow flowers"></div>

<section>
  <h1 class="consult-title heading abs">Free In-Home Consultation<br>We're Here to Listen,<br>Learn, and Help</h1>
  <p class="consult-lede abs">Since every living situation is different and every client has specific needs, we like to meet with you in person.</p>
  <div class="call-button abs">Call Us: 555-210-318</div>
  <div class="consult-photo photo-frame abs" role="img" aria-label="Young caregiver cheek to cheek with an elderly woman"></div>
</section>

<section class="services abs"></section>
<div class="services-photo abs" role="img" aria-label="Caregiver helping a senior woman in a blue dress down the stairs"></div>
<h2 class="services-title heading abs">Our Services</h2>
<p class="services-intro abs">Larkmoor Home Care offers a wide variety of home care services, from once a week visits to 24-hour care. Since every situation is unique, we work together with you to create the perfect program.</p>
<p class="services-body abs">Here is just a short list of the services we provide. Don't worry about pricing or deciphering a confusing invoice. All of these services are included in our simple One Flat Rate price structure.</p>
<ul class="service-list abs">
  <li><svg width="20" height="20" viewBox="0 0 20 20" aria-hidden="true"><circle cx="10" cy="10" r="10" fill="#2ca6df"/><path d="M6 10h7M10 6.5l3.5 3.5-3.5 3.5" stroke="#fff" stroke-width="2" fill="none"/></svg>Companionship</li>
  <li><svg width="20" height="20" viewBox="0 0 20 20" aria-hidden="true"><circle cx="10" cy="10" r="10" fill="#2ca6df"/><path d="M6 10h7M10 6.5l3.5 3.5-3.5 3.5" stroke="#fff" stroke-width="2" fill="none"/></svg>Personal Care</li>
  <li><svg width="20" height="20" viewBox="0 0 20 20" aria-hidden="true"><circle cx="10" cy="10" r="10" fill="#2ca6df"/><path d="M6 10h7M10 6.5l3.5 3.5-3.5 3.5" stroke="#fff" stroke-width="2" fill="none"/></svg>Dementia &amp; Alzheimer's Care</li>
  <li><svg width="20" height="20" viewBox="0 0 20 20" aria-hidden="true"><circle cx="10" cy="10" r="10" fill="#2ca6df"/><path d="M6 10h7M10 6.5l3.5 3.5-3.5 3.5" stroke="#fff" stroke-width="2" fill="none"/></svg>Housekeeping</li>
  <li><svg width="20" height="20" viewBox="0 0 20 20" aria-hidden="true"><circle cx="10" cy="10" r="10" fill="#2ca6df"/><path d="M6 10h7M10 6.5l3.5 3.5-3.5 3.5" stroke="#fff" stroke-width="2" fill="none"/></svg>Transportation</li>
</ul>
<p class="services-close abs">There's much more we can do to help. Please call us to schedule free in-home consultation.</p>

<h2 class="welcome-title heading abs">Welcome to Our Website</h2>
<div class="welcome-copy abs">
  <p>Larkmoor Home Care is a local family owned and operated agency devoted to helping families like yours in the Inland Empire. We take pride in the relationships we develop with our clients. We understand this is a challenging time and we are dedicated to providing the peace of mind you deserve. At Larkmoor Home Care we do more than just watch your loved ones. We care for them with programs designed to keep them both mentally and physically comfortable, happy and healthy</p>
  <p>Being a family agency is what makes Larkmoor Home Care special and sets us apart. We treat our caregivers as part of the family too. They are paid more than the average care giver and receive year round continuing education, exceeding state mandated minimum standards by miles.</p>
</div>

<section class="contact abs"></section>
<h2 class="contact-title heading abs">Contact Us</h2>
<p class="contact-sub abs">Please call us at: 555-210-3180 or fill out the form</p>
<div class="field abs" style="left:256px;top:2455px;width:339px;height:47px">Name<svg width="14" height="14" viewBox="0 0 14 14" aria-hidden="true"><circle cx="7" cy="4" r="3" fill="#777"/><path d="M1 13c0-3 3-5 6-5s6 2 6 5z" fill="#777"/></svg></div>
<div class="field abs" style="left:256px;top:2511px;width:339px;height:47px">Email<svg width="14" height="14" viewBox="0 0 14 14" aria-hidden="true"><rect x="1" y="3" width="12" height="8" fill="none" stroke="#777"/><path d="M1 3l6 5 6-5" fill="none" stroke="#777"/></svg></div>
<div class="field abs" style="left:256px;top:2570px;width:339px;height:47px">Phone<svg width="14" height="14" viewBox="0 0 24 24" aria-hidden="true"><path d="M6.6 10.8c1.4 2.8 3.8 5.1 6.6 6.6l2.2-2.2c.3-.3.7-.4 1-.2 1.1.4 2.3.6 3.6.6.6 0 1 .4 1 1V20c0 .6-.4 1-1 1C10.6 21 3 13.4 3 4c0-.6.4-1 1-1h3.5c.6 0 1 .4 1 1 0 1.3.2 2.5.6 3.6.1.3 0 .7-.2 1z" fill="#777"/></svg></div>
<div class="field abs" style="left:604px;top:2455px;width:337px;height:160px">Message<svg width="16" height="14" viewBox="0 0 16 14" aria-hidden="true"><rect x="1" y="1" width="9" height="6" fill="#777"/><rect x="6" y="5" width="9" height="6" fill="#999"/></svg></div>
<div class="submit abs">Submit</div>

<footer class="site-footer abs">
  <p class="copyright abs">Copyright © 2016 . All rights reserved.</p>
  <span class="social abs" style="left:1007px;background:#3b5998"></span>
  <span class="social abs" style="left:1041px;background:#1da1f2"></span>
  <span class="social abs" style="left:1075px;background:#dd4b39"></span>
  <span class="social abs" style="left:1109px;background:#0e76a8"></span>
</footer>

</body>
</html>
```